Letterhead for denture company

We need a letterhead designed for our denture company called "Brightbite" We have attached the logo and business card with the colours on them that we like

Target Market(s)

Everyone aged 45+

Industry/Entity Type

Dental Clinic

Font styles to use
Serif
Sans Serif

Colors
3276b5
f37122

Requirements
Must have
• The colours used in our business card
• Be bold and modern
• Thick fonts
• Logo
Nice to have
• Elements that could tie in nicely with any future signage or website upgrades
Should not have
• Thin font
• Should not be too busy

```html
<!DOCTYPE html>
<html lang="en">
<head>
<meta charset="utf-8">
<title>Brightbite Letterhead</title>
<link href="https://fonts.googleapis.com/css2?family=Lato:wght@400;700;900&display=swap" rel="stylesheet">
<style>
  :root {
    --brand-blue: #1f6fb2;
    --brand-orange: #f37122;
    --paper: #f4f4f4;
    --backdrop: #d9d9d9;
    --ink: #1d1d1d;
    --white: #ffffff;
  }
  * { box-sizing: border-box; margin: 0; padding: 0; }
  html, body { width: 1187px; height: 1200px; overflow: hidden; }
  body {
    background: var(--backdrop);
    font-family: "Lato", Arial, sans-serif;
    color: var(--ink);
  }
  .letterhead {
    position: absolute;
    left: 197px;
    top: 40px;
    width: 792px;
    height: 1120px;
    background: var(--paper);
    box-shadow: 0 10px 30px rgba(0,0,0,0.15);
    overflow: hidden;
  }
  .sidebar {
    position: absolute;
    left: 0; top: 0;
    width: 160px; height: 1120px;
  }
  .brand {
    position: absolute;
    left: 160px; right: 0;
    top: 110px;
    display: flex;
    justify-content: center;
    align-items: center;
    gap: 12px;
  }
  .brand-square {
    display: block;
    width: 34px; height: 34px;
    background: var(--brand-blue);
    border-radius: 3px;
  }
  .brand-name {
    font-weight: 900;
    font-size: 32px;
    letter-spacing: 1px;
    color: var(--brand-blue);
    line-height: 1;
  }
  .recipient {
    position: absolute;
    left: 228px;
    top: 228px;
  }
  .recipient-name {
    font-weight: 900;
    font-size: 20px;
    color: var(--brand-orange);
  }
  .recipient-address {
    margin-top: 3px;
    font-weight: 700;
    font-size: 10.5px;
    line-height: 1.3;
  }
  .letter-body {
    position: absolute;
    left: 212px;
    top: 378px;
    width: 505px;
    font-size: 11px;
    line-height: 1.45;
  }
  .letter-body p { margin-bottom: 15px; }
  .sign-off {
    position: absolute;
    left: 205px;
    top: 925px;
    font-weight: 700;
    font-size: 10.5px;
  }
  .sign-off .signatory { margin-top: 22px; }
  .sidebar-contact {
    position: absolute;
    left: 22px;
    top: 955px;
    color: var(--white);
    font-size: 10px;
    line-height: 1.3;
    font-style: normal;
  }
  .sidebar-contact .group { margin-bottom: 14px; }
</style>
</head>
<body>
  <main class="letterhead">
    <svg class="sidebar" viewBox="0 0 160 1120" aria-hidden="true">
      <path d="M0 0 H120 V880 Q120 895 132 905 Q146 918 146 935 V1120 H0 Z" fill="var(--brand-blue)"/>
      <path d="M127 0 V876 Q127 890 139 900 Q153 912 153 932 V1120" fill="none" stroke="var(--brand-orange)" stroke-width="4"/>
    </svg>

    <header class="brand">
      <span class="brand-square"></span>
      <div class="brand-name">Brightbite</div>
    </header>

    <section class="recipient">
      <div class="recipient-name">Jane Doe</div>
      <div class="recipient-address">48 Harbour View Road<br>Westmere Heights,<br>Auckland 0614</div>
    </section>

    <article class="letter-body">
      <p>Lorem ipsum dolor sit amet, consectetur adipiscing elit. Cras iaculis dictum arcu, fermentum bibendum eros facilisis sit amet. Cras in tellus velit. Nam venenatis massa ut molestie maximus. Pellentesque tincidunt venenatis lectus, in aliquet metus blandit ac. Sed lacinia quis arcu ac feugiat. Pellentesque posuere ultricies tortor, vel eleifend ante feugiat id. Nam interdum finibus arcu, ornare sollicitudin enim pellentesque sit amet. Ut sed dolor vel neque feugiat feugiat. Quisque rutrum aliquam neque, in iaculis ipsum sagittis in. Nunc luctus, arcu ac ullamcorper egestas, metus massa sodales metus, sit amet placerat erat ipsum ut enim. Duis nec dui egestas erat posuere malesuada vitae at metus. Etiam ullamcorper, lacus ac eleifend lobortis, libero lorem aliquet libero, in venenatis tortor ex lacinia risus. Suspendisse potenti.</p>
      <p>Nullam convallis, ligula eget vehicula sagittis, lorem leo maximus nulla, ac eleifend diam lectus eu enim. Integer vitae lorem sit amet ligula sollicitudin placerat et non massa. Etiam porta massa quis dignissim tincidunt. Vivamus est justo, pellentesque eu dignissim eu, aliquet pulvinar nisl. Praesent a efficitur lorem, ut efficitur nulla. In a eros sed velit commodo tempus. Praesent eget efficitur magna. Etiam bibendum vel justo vitae finibus.</p>
      <p>Sed interdum placerat ultricies. Donec pretium arcu a aliquet sollicitudin. Integer aliquet ligula accumsan consectetur aliquam. Donec non rutrum augue. Nunc non pellentesque urna, eget blandit diam. Proin in efficitur mi. Ut vel placerat lectus. Praesent scelerisque leo sed sollicitudin finibus. Cras sed laoreet felis, et maximus odio. Pellentesque mattis quis dolor ac convallis. Pellentesque vehicula massa dui, quis malesuada eros facilisis in.</p>
      <p>Nunc in malesuada ante. Duis pulvinar maximus auctor. Fusce vel lorem sodales, bibendum lorem ac, finibus ipsum. Sed eu velit in metus gravida maximus. Donec interdum enim metus, vitae sollicitudin nunc rutrum ac. Quisque non arcu massa. Vivamus tempus erat ut sem ultrices, vel egestas lorem consequat.</p>
      <p>Nam vulputate lacus sollicitudin arcu facilisis, quis tempor augue maximus. Aliquam in sem convallis, finibus velit ac, tempor magna. Nulla eget dui tortor. Integer in gravida libero, nec fermentum orci. Mauris malesuada elit non tellus tristique, eu blandit tellus ultricies. Nam lobortis magna lectus, ut ullamcorper quam dignissim sed. Donec rhoncus leo lorem. Maecenas sit amet nisi id quam auctor gravida. Nullam vel urna vel neque blandit suscipit. Morbi venenatis ligula sed tortor vestibulum varius non eu mauris. Nullam laoreet sit amet lacus et volutpat. Morbi egestas, ante sit amet laoreet bibendum, augue dolor pretium velit, a consectetur risus ante a risus. Duis fringilla sagittis tristique. Sed finibus orci sed augue mollis finibus. Proin tempor tempor felis quis scelerisque. Donec sed varius felis.</p>
    </article>

    <footer class="sign-off">
      <div>Sincerely,</div>
      <div class="signatory">Joe Brightbite</div>
    </footer>

    <address class="sidebar-contact">
      <div class="group">48 Harbour View Road<br>Westmere Heights,<br>Auckland 0614</div>
      <div class="group">P: 0800 55 2100<br>C: 09 512 4470</div>
      <div class="group">www.brightbite.co.nz<br>joe@brightbite.co.nz</div>
    </address>
  </main>
</body>
</html>
```